engaging mobile application to encourage lifestyle change

We need an App that will help people get from Bloom 4 Joy. A weight loss program based on realistic and healthy lifestyle modifications. By learning portion control, healthy food choices, and with the encouragement to get moving.
We would like the design to be gender neutral but must be fun.
The final design must be easy to use and useful to our clients.

Target Market(s)

Health, Wellbeing, Weightloss

Industry/Entity Type

Weight

Font styles to use
Sans Serif

Requirements
Must have
• Hydration log, Weigh-ins with fat %, Food log, Location of meetings,lectures and weigh-ins, list of restaurants that comply with B4J, Fitness plan, Mall walk maps, daily motivational message.

```html
<!DOCTYPE html>
<html lang="en">
<head>
<meta charset="utf-8">
<title>Nutrient Insights</title>
<link href="https://fonts.googleapis.com/css2?family=Roboto:wght@400;500&display=swap" rel="stylesheet">
<style>
  :root {
    --status-purple: #5b3bbf;
    --appbar-orange: #ff9a0a;
    --chart-bg: #f0f0f2;
    --grid: #d4d4d8;
    --bar-light: #a9defb;
    --bar-mid: #5dbcf6;
    --bar-dark: #3f94d6;
    --axis: #1d1d1d;
    --label: #2b2b2b;
    --accent: #ff9a0a;
    --fat-day: #cbd6e5;
    --fat-week: #97b3d3;
    --fat-month: #6489b6;
    --white: #ffffff;
  }
  html, body { margin: 0; padding: 0; overflow: hidden; }
  body { width: 750px; height: 1200px; background: var(--white); font-family: 'Roboto', sans-serif; position: relative; }
  .status-bar { height: 62px; background: var(--status-purple); color: var(--white); display: flex; justify-content: flex-end; align-items: center; padding-right: 18px; gap: 10px; font-size: 24px; font-weight: 500; box-sizing: border-box; }
  .app-bar { height: 88px; background: var(--appbar-orange); display: flex; align-items: center; padding-left: 10px; gap: 10px; color: var(--white); }
  .app-bar .back { font-size: 30px; opacity: .7; }
  .app-bar .brand-mark { width: 58px; height: 58px; border: 4px solid var(--white); border-radius: 9px; box-sizing: border-box; }
  .app-bar h1 { margin: 0; font-size: 36px; font-weight: 400; }
  .insights { position: absolute; top: 150px; left: 0; }
  .axis-label { font-size: 22px; fill: var(--label); }
  .day-label { font-size: 27px; fill: var(--label); }
  .day-num { font-size: 19px; fill: var(--label); }
  .legend-text { font-size: 23px; fill: var(--label); }
  .fat-value { font-size: 24px; fill: var(--label); }
</style>
</head>
<body>
  <header class="status-bar">
    <svg width="26" height="22" viewBox="0 0 26 22" aria-hidden="true"><polygon points="26,0 26,22 0,22" fill="#fff"/></svg>
    <svg width="16" height="26" viewBox="0 0 16 26" aria-hidden="true"><rect x="0" y="3" width="16" height="23" rx="1.5" fill="#fff"/><rect x="5" y="0" width="6" height="4" fill="#fff"/></svg>
    <span class="clock">4:37</span>
  </header>
  <div class="app-bar">
    <span class="back">&#8249;</span>
    <span class="brand-mark" aria-hidden="true"></span>
    <h1>Nutrient Insights</h1>
  </div>

  <svg class="insights" width="750" height="1050" viewBox="0 150 750 1050">
    <!-- chart area -->
    <rect class="chart-bg" x="0" y="150" width="750" height="629" fill="var(--chart-bg)"/>
    <g class="gridlines" stroke="var(--grid)" stroke-width="1.5">
      <line x1="0" y1="255" x2="623" y2="255"/><line x1="0" y1="299" x2="623" y2="299"/>
      <line x1="0" y1="342" x2="623" y2="342"/><line x1="0" y1="386" x2="623" y2="386"/>
      <line x1="0" y1="430" x2="623" y2="430"/><line x1="0" y1="473" x2="623" y2="473"/>
      <line x1="0" y1="517" x2="623" y2="517"/><line x1="0" y1="561" x2="623" y2="561"/>
      <line x1="0" y1="604" x2="623" y2="604"/><line x1="0" y1="648" x2="623" y2="648"/>
      <line x1="0" y1="692" x2="623" y2="692"/><line x1="0" y1="735" x2="623" y2="735"/>
      <line x1="222" y1="237" x2="222" y2="779"/>
    </g>
    <g class="axis-labels">
      <text class="axis-label" x="631" y="263">2,400</text><text class="axis-label" x="631" y="307">2,200</text>
      <text class="axis-label" x="631" y="350">2,000</text><text class="axis-label" x="631" y="394">1,800</text>
      <text class="axis-label" x="631" y="438">1,600</text><text class="axis-label" x="631" y="481">1,400</text>
      <text class="axis-label" x="631" y="525">1,200</text><text class="axis-label" x="631" y="569">1,000</text>
      <text class="axis-label" x="631" y="612">800</text><text class="axis-label" x="631" y="656">600</text>
      <text class="axis-label" x="631" y="700">400</text><text class="axis-label" x="631" y="743">200</text>
    </g>
    <g class="bars">
      <rect x="0" y="342" width="84" height="437" fill="var(--bar-light)"/>
      <rect x="0" y="430" width="84" height="349" fill="var(--bar-mid)"/>
      <rect x="0" y="648" width="84" height="131" fill="var(--bar-dark)" opacity=".85"/>

      <rect x="88" y="384" width="102" height="395" fill="var(--bar-light)"/>
      <rect x="88" y="447" width="102" height="332" fill="var(--bar-mid)"/>
      <rect x="88" y="589" width="102" height="190" fill="var(--bar-dark)" opacity=".85"/>

      <rect x="253" y="430" width="103" height="349" fill="var(--bar-light)"/>
      <rect x="253" y="532" width="103" height="247" fill="var(--bar-mid)"/>
      <rect x="253" y="692" width="103" height="87" fill="var(--bar-dark)"/>

      <rect x="360" y="462" width="102" height="317" fill="var(--bar-light)"/>
      <rect x="360" y="539" width="102" height="240" fill="var(--bar-mid)"/>
      <rect x="360" y="700" width="102" height="79" fill="var(--bar-dark)"/>

      <rect x="464" y="609" width="103" height="170" fill="var(--bar-light)"/>
      <rect x="464" y="657" width="103" height="122" fill="var(--bar-mid)"/>
      <rect x="464" y="731" width="103" height="48" fill="var(--bar-dark)"/>
    </g>
    <g class="baseline">
      <polyline points="0,779 464,779 517,731 567,779 623,779" fill="none" stroke="var(--axis)" stroke-width="2"/>
      <polygon points="466,780 517,733 565,780" fill="var(--white)"/>
      <text x="504" y="773" font-size="26" fill="var(--accent)">W</text>
    </g>
    <g class="day-labels">
      <text class="day-label" x="0" y="778">Sa</text><text class="day-num" x="42" y="767">27</text>
      <text class="day-label" x="104" y="778">Su</text><text class="day-num" x="146" y="767">28</text>
      <text class="day-label" x="274" y="778">M</text><text class="day-num" x="308" y="767">29</text>
      <text class="day-label" x="379" y="778">Tu</text><text class="day-num" x="418" y="767">30</text>
    </g>

    <!-- legend -->
    <g class="legend">
      <rect x="21" y="852" width="24" height="22" rx="2" fill="var(--fat-day)"/>
      <text class="legend-text" x="54" y="873">Wed Dec 31 2014</text>
      <rect x="21" y="884" width="24" height="22" rx="2" fill="var(--fat-week)"/>
      <text class="legend-text" x="54" y="905">Average for last 7 days</text>
      <rect x="21" y="915" width="24" height="22" rx="2" fill="var(--fat-month)"/>
      <text class="legend-text" x="54" y="936">Average for last 28 days</text>
    </g>

    <!-- fat comparison -->
    <g class="fat-chart">
      <g stroke="var(--grid)" stroke-width="1.5">
        <line x1="31" y1="967" x2="31" y2="1200"/><line x1="219" y1="967" x2="219" y2="1200"/>
        <line x1="407" y1="967" x2="407" y2="1200"/><line x1="595" y1="967" x2="595" y2="1200"/>
      </g>
      <text class="legend-text" x="40" y="992">Fat</text>
      <rect x="31" y="1006" width="218" height="53" fill="var(--fat-day)"/>
      <text class="fat-value" x="279" y="1041">232 cals</text>
      <rect x="31" y="1065" width="452" height="53" fill="var(--fat-week)"/>
      <text class="fat-value" x="512" y="1100">480 cals</text>
      <rect x="31" y="1124" width="270" height="53" fill="var(--fat-month)"/>
      <text class="fat-value" x="333" y="1159">287 cals</text>
    </g>
  </svg>
</body>
</html>
```